Stationary

We have designed a new logo and business care.
It is now time for stationary.
We are a financial planning firm and are looking for something more formal that show the strength of our firm.
Please include our tag line; Clarity - Strength -Stewardship.
I have uploaded a PDF of our current stationary - but - you are under no obligation to design anything like it.
Thx
Marta
Business

```html
<!DOCTYPE html>
<html lang="en">
<head>
<meta charset="utf-8">
<title>Northbridge Capital Group — Stationery</title>
<link rel="stylesheet" href="https://fonts.googleapis.com/css2?family=PT+Sans:wght@400;700&display=swap">
<style>
  :root {
    --brand-blue: #35468f;
    --paper: #fbfbfb;
    --backdrop: #eeeeee;
    --ink: #4a4a4a;
    --ink-soft: #6b6b6b;
    --white: #ffffff;
  }
  * { box-sizing: border-box; margin: 0; padding: 0; }
  html, body {
    width: 1200px; height: 1005px; overflow: hidden;
    background: var(--backdrop);
    font-family: "PT Sans", Arial, sans-serif;
  }
  address { font-style: normal; }
  .stationery-set { position: relative; width: 1200px; height: 1005px; }

  .brand-mark {
    display: flex; align-items: center; gap: 5px;
    color: var(--brand-blue); font-weight: 400; white-space: nowrap;
  }
  .brand-mark .brand-dot {
    width: 9px; height: 9px; border-radius: 50%; background: var(--brand-blue); flex: none;
  }
  .tagline { font-weight: 700; white-space: nowrap; }

  /* Letterhead */
  .letterhead {
    position: absolute; left: 167px; top: 84px; width: 400px; height: 568px;
    background: var(--paper);
  }
  .letterhead .brand-mark { position: absolute; left: 37px; top: 44px; font-size: 11px; }
  .sender-details {
    position: absolute; right: 34px; top: 32px; text-align: right;
    font-size: 7px; line-height: 9.4px; color: var(--ink-soft);
  }
  .sender-details .label { color: var(--brand-blue); }
  .sender-details .web { color: var(--brand-blue); font-weight: 700; }
  .salutation {
    position: absolute; left: 37px; top: 157px; font-size: 12px; color: var(--ink);
  }
  .letter-body {
    position: absolute; left: 37px; top: 193px; width: 329px;
    font-size: 6.4px; line-height: 9.6px; color: var(--ink-soft); text-align: justify;
  }
  .letter-body p { margin-bottom: 9.6px; }
  .sign-off { position: absolute; left: 37px; top: 402px; font-size: 6.4px; color: var(--ink-soft); }
  .signature {
    position: absolute; left: 35px; top: 417px; width: 54px; height: 20px;
    background: #e6e6e6; border-radius: 2px;
  }
  .letterhead .tagline {
    position: absolute; left: 0; right: 0; top: 538px; text-align: center;
    font-size: 10px; color: var(--brand-blue);
  }

  /* Presentation folder */
  .folder {
    position: absolute; left: 637px; top: 58px; width: 471px; height: 598px;
    background: var(--brand-blue);
  }
  .folder .spine {
    position: absolute; left: 0; top: 0; bottom: 0; width: 12px;
    border-right: 1px solid rgba(255,255,255,0.12);
  }
  .folder .brand-mark {
    position: absolute; left: 0; right: 0; top: 270px; justify-content: center;
    color: var(--white); font-size: 22px; gap: 9px;
  }
  .folder .brand-mark .brand-dot { width: 16px; height: 16px; background: var(--white); }
  .folder .tagline {
    position: absolute; left: 0; right: 0; top: 561px; text-align: center;
    font-size: 12px; color: var(--white);
  }

  /* Envelope back (return address) */
  .envelope-back {
    position: absolute; left: 167px; top: 714px; width: 448px; height: 218px;
    background: var(--paper);
  }
  .envelope-back .brand-mark { position: absolute; left: 26px; top: 54px; font-size: 10px; }
  .return-address {
    position: absolute; left: 26px; top: 69px; font-size: 5.6px; color: var(--ink-soft);
  }

  /* Envelope front with flap */
  .envelope-front {
    position: absolute; left: 659px; top: 716px; width: 448px; height: 212px;
    background: var(--paper);
  }
  .envelope-front .flap { position: absolute; left: 0; top: 0; }
  .envelope-front .brand-mark {
    position: absolute; left: 0; right: 0; top: 24px; justify-content: center;
    color: var(--white); font-size: 9px; gap: 4px;
  }
  .envelope-front .brand-mark .brand-dot { width: 7px; height: 7px; background: var(--white); }
  .envelope-front .tagline {
    position: absolute; left: 0; right: 0; top: 45px; text-align: center;
    font-size: 7.5px; color: var(--white);
  }
</style>
</head>
<body>
<main class="stationery-set">

  <section class="letterhead" aria-label="Letterhead">
    <div class="brand-mark"><span class="brand-dot"></span>Northbridge Capital Group</div>
    <address class="sender-details">
      2750 W. Alder Ave.<br>
      Boise, ID 83702<br>
      <span class="label">Tel</span> (208) 555-0142<br>
      <span class="label">Fax</span> (208) 555-0143<br>
      <span class="label">Email</span> name@ncg.com<br>
      <span class="web">www.ncg.com</span>
    </address>

    <p class="salutation">Dear Mr. Hale,</p>
    <div class="letter-body">
      <p>Thank you for meeting with our planning team last week. We have reviewed your retirement goals, current holdings and income needs, and prepared a clear outline of the next steps we recommend. Our advisors will walk you through each option in detail, explain the costs and benefits of every choice, and answer any questions so you can decide with full confidence.</p>
      <p>Enclosed you will find a summary of your portfolio, a projected savings schedule and a comparison of the accounts we discussed. Please review these documents at your convenience and note any questions you would like to raise at our next meeting. We will also confirm the tax details with your accountant before any changes are made.</p>
      <p>Our approach rests on careful research and steady guidance. We monitor market conditions closely, rebalance when needed and keep you informed with regular written reports. Every recommendation we make is built around your long-term interests, your tolerance for risk and the lasting security of your family and estate.</p>
      <p>We value the trust you have placed in our firm. If you have any questions before our next meeting, please call our office and a member of our team will gladly assist you.</p>
    </div>
    <p class="sign-off">Sincerely,</p>
    <div class="signature" role="img" aria-label="Handwritten signature"></div>

    <p class="tagline">Clarity - Strength -Stewardship.</p>
  </section>

  <section class="folder" aria-label="Presentation folder cover">
    <div class="spine"></div>
    <div class="brand-mark"><span class="brand-dot"></span>Northbridge Capital Group</div>
    <p class="tagline">Clarity - Strength -Stewardship.</p>
  </section>

  <section class="envelope-back" aria-label="Envelope with return address">
    <div class="brand-mark"><span class="brand-dot"></span>Northbridge Capital Group</div>
    <address class="return-address">2750 W. Alder Ave. Boise, ID 83702</address>
  </section>

  <section class="envelope-front" aria-label="Envelope flap">
    <svg class="flap" width="448" height="86" viewBox="0 0 448 86" aria-hidden="true">
      <path d="M0 0 H448 V62 Q448 78 432 82 H16 Q0 82 0 66 Z" fill="var(--brand-blue)"/>
    </svg>
    <div class="brand-mark"><span class="brand-dot"></span>Northbridge Capital Group</div>
    <p class="tagline">Clarity - Strength -Stewardship.</p>
  </section>

</main>
</body>
</html>
```